Concept design for a tea business Labels

Hello, we are looking for concepts for our label/packaging for a tea business that has been in business now for over a year. We are a beachy, organic, "It's your moment. Enjoy it." type tea business. We have an online website (www.driftleafbrews.com.au) and sell at local markets around the Corvel Cove area.
We are looking to upgrade our label to look more professional, in a fun/beachy/chilled out style. (unlike the traditional tea labels).
We do loose leaf tea and iced tea consentrated syrups. We have a few different packages (please see website under "sizes and packaging" bottom left). We would like to experiement with various different size and shape of labels for different products, so would like a concept design for a label using our logo (see website front page bottom). There are no colour constraints.
We use the Norvik brand labels of the following sizes:
1. Pure Glint Rectangular Product Labels, Q4826, 100/Pack, 96 x 50.8 mm
2. Pure Glint Round Multi-purpose Labels, Q3957D, 240/Pack, 40 mm diameter
3.Pure Glint Square Product Labels, Q4861, 350/Pack, 35 x 35 mm
4. For bottles we use Grained Ivory Domed Labels, Q4839, 90/Pack, 57.2 x 77 mm
If you have any more questions, please don't hesitate to contact me
Updates
Hi All,
I am considering using a box like below for packing and doing a bit of a white/beachy feel to the packaging. Either using the rectangle or round circle labels. (circle labels from norvik 60mm diameter).

Reason: Hi All - Thank you so much for all your designs. While I have seen some really beautiful designs I am excited about, it seems there was a rush at the end with a number of new designs just submitted. I still haven't seen just one design I love for the label, so I would like the opportunity to work with some of the new designers to see if we can modify to suit the concept.
Would anyone like to try a concept label with a silhouette of one of the following wave/beach/teacup? I'm just exploring a different approach as I know it is difficult tying in the beach with tea - please think - chilled out beach hut with tea/iced tea, sunrise over ocean. I like the soft colour palette - beachy feel to it - ie. Pastels - blues, greens, whites, sandy, pinks, purples, greys - sunrises over ocean, maybe a white rustic wood feel - or any other icon from Corvel Cove - like the Norfolk Pine's along the beach - maybe in Silhouette.
Just some more ideas.
Thank you again for all your contributions!
Greta

```html
<!DOCTYPE html>
<html lang="en">
<head>
<meta charset="utf-8">
<title>Cranberry &amp; Lime Organic Ice Tea – Bottle Label</title>
<link rel="stylesheet" href="https://fonts.googleapis.com/css2?family=Crimson+Text:wght@400;600&display=swap">
<style>
  :root {
    --canvas-bg: #ffffff;
    --label-green: #d4d66b;
    --label-cream: #fdf8df;
    --wave-light: #fbf4d2;
    --wave-shade: #eee5b2;
    --ink-olive: #5b5a3a;
    --ink-body: #4e4d33;
    --organic-cream: #fffbe6;
  }
  * { box-sizing: border-box; margin: 0; padding: 0; }
  html, body {
    width: 1200px; height: 1200px; overflow: hidden;
    background: var(--canvas-bg);
  }
  .canvas {
    position: relative; width: 1200px; height: 1200px;
    display: flex; align-items: center; justify-content: center;
  }
  .bottle-label {
    position: relative; width: 580px; height: 1100px;
    border-radius: 30px; overflow: hidden;
    background: var(--label-cream);
    font-family: "Crimson Text", "Times New Roman", serif;
    color: var(--ink-olive);
  }
  .label-field {
    position: absolute; inset: 0; width: 100%; height: 100%;
  }
  .flavour-title {
    position: absolute; left: 38px; top: 42px;
    font-weight: 400; letter-spacing: 0.5px; white-space: nowrap;
  }
  .flavour-title .flavour-line {
    display: block; font-size: 76px; line-height: 70px;
  }
  .flavour-title .organic-line {
    display: block; font-size: 86px; line-height: 80px;
    color: var(--organic-cream);
  }
  .product-name {
    position: absolute; left: 40px; top: 300px;
    font-size: 124px; line-height: 100px; font-weight: 400;
    letter-spacing: 1px;
  }
  .product-name span { display: block; }
  .product-name .tea-word { margin-left: -6px; }
  .net-weight {
    position: absolute; right: 16px; top: 430px;
    font-size: 22px; writing-mode: vertical-rl;
    color: var(--ink-olive);
  }
  .label-copy {
    position: absolute; left: 40px; right: 38px; top: 612px;
    font-size: 16px; line-height: 20px; text-align: justify;
    color: var(--ink-body);
  }
  .label-copy p + p { margin-top: 20px; }
  .label-footer {
    position: absolute; left: 40px; right: 34px; bottom: 34px;
    display: flex; align-items: center; justify-content: space-between;
  }
  .company-name {
    font-size: 28px; letter-spacing: 0.5px; color: var(--ink-olive);
  }
  .company-mark {
    width: 104px; height: 104px; border-radius: 50%;
    background: var(--label-green);
  }
</style>
</head>
<body>
<main class="canvas">
  <article class="bottle-label">
    <svg class="label-field" viewBox="0 0 580 1100" preserveAspectRatio="none">
      <defs>
        <linearGradient id="wave-tone" x1="0" y1="0" x2="1" y2="1">
          <stop offset="0" stop-color="var(--wave-light)"/>
          <stop offset="1" stop-color="var(--wave-shade)"/>
        </linearGradient>
      </defs>
      <path class="label-band" fill="var(--label-green)"
        d="M0 0 H580 V430 C520 520 380 580 0 565 Z"/>
      <rect class="wave-placeholder" role="img" aria-label="Curling cream ocean wave illustration"
        x="380" y="290" width="150" height="230" rx="40" fill="url(#wave-tone)"/>
    </svg>

    <h1 class="flavour-title">
      <span class="flavour-line">CRANBERRY</span>
      <span class="flavour-line">&amp; LIME</span>
      <span class="organic-line">ORGANIC</span>
    </h1>

    <h2 class="product-name">
      <span class="ice-word">ICE</span>
      <span class="tea-word">TEA</span>
    </h2>

    <p class="net-weight">8 Oz / 250g</p>

    <section class="label-copy">
      <p>Our iced tea is brewed slowly from organic leaves, then blended with tart cranberry and a squeeze of fresh lime for a bright, easy finish. Keep it chilled, shake the bottle well and pour it over plenty of ice. Best enjoyed with sand between your toes, a warm breeze and nowhere else to be. It's your moment, so slow right down and enjoy every single sip of it today.</p>
      <p>Ingredients: filtered water, organic black tea, organic cranberry juice, organic lime juice and raw cane sugar. Made in small batches close to the shore. Refrigerate after opening and consume within five days. Contains no artificial colours, flavours or preservatives. Natural sediment may settle at the bottom of the bottle.</p>
    </section>

    <footer class="label-footer">
      <span class="company-name">CORVEL TEA COMPANY</span>
      <span class="company-mark" aria-hidden="true"></span>
    </footer>
  </article>
</main>
</body>
</html>
```